Redesign of a Restaurant web presence

We need a new design of our restaurant web page which can also be based on a new CI (current main colours are gold, green and pink/violett), urban jungle style.
WORDPRESS is being used for coding the website and there should be no monthly paid plug-ins be used.
Main features should be the presentation of our location, downloadable menus (pdf), a possibility for online reservations (pop-up on start page) and recruitung staff (job descriptions to be viewed).
Focus should be on the design, functionality is very basic.
Multi language preferred (SK,DE,EN).
Working on desktop and mobile devices.
A reference site is moravel.at
Current page dulmirotable.sk
If the co-operation is good, we also need template layouts for our new printed menu based on the (new) CI.
Designs look the same

```html
<!DOCTYPE html>
<html lang="sk">
<head>
<meta charset="utf-8">
<title>Dulmiro Table – Café & Restaurant</title>
<link href="https://fonts.googleapis.com/css2?family=Cinzel:wght@500;700&family=Quicksand:wght@400;500;600&display=swap" rel="stylesheet">
<style>
:root{
  --gold:#d4b20c;
  --ink:#1a1a1a;
  --dark:#1b1c22;
  --muted:#7a7a7a;
  --line:#e6e6e6;
  --white:#ffffff;
  --black:#000000;
}
*{box-sizing:border-box;margin:0;padding:0}
html,body{width:1200px;height:2727px;overflow:hidden}
body{font-family:'Quicksand',sans-serif;color:var(--ink);background:var(--white);position:relative}
.serif{font-family:'Cinzel',serif}
section,header,footer{position:absolute;left:0;width:1200px}
.btn{display:inline-flex;align-items:center;justify-content:center;background:var(--gold);color:var(--ink);font-size:15px;font-weight:500}

/* header */
.site-header{top:0;height:85px;background:var(--white)}
.brand{position:absolute;left:57px;top:26px;width:108px;text-align:center}
.brand-name{font-family:'Cinzel',serif;font-size:14px;letter-spacing:.5px;line-height:1;display:block}
.brand-sub{font-size:6px;letter-spacing:1.5px;display:block;margin-top:3px;border-top:1px solid var(--ink);padding-top:2px}
.nav{position:absolute;left:196px;top:33px;display:flex;gap:28px;font-family:'Cinzel',serif;font-size:14px}
.nav .active{color:var(--gold)}
.nav .drop::after{content:"▾";margin-left:18px;font-size:11px}
.btn-contact{position:absolute;left:1036px;top:20px;width:110px;height:45px;font-family:'Cinzel',serif;font-size:13px}

/* hero */
.hero{top:85px;height:471px}
.hero-photo{position:absolute;inset:0;background:linear-gradient(180deg,#6c5d47 0%,#8a7c66 35%,#2f6f78 62%,#1f5a66 80%,#a69a8a 100%)}
.hero-shade{position:absolute;inset:0;background:rgba(0,0,0,.25)}
.hero-title{position:absolute;top:125px;width:100%;text-align:center;color:var(--white);font-family:'Cinzel',serif;font-weight:700;font-size:40px;line-height:56px}
.hero-btn{position:absolute;left:472px;top:300px;width:256px;height:41px;font-size:15px}

/* reservation */
.reserve{top:556px;height:371px}
.reserve h2{position:absolute;left:117px;top:50px;font-family:'Cinzel',serif;font-weight:500;font-size:25px;line-height:37px}
.reserve p{position:absolute;left:117px;top:141px;font-size:13px;line-height:20px;width:240px}
.btn-send{position:absolute;left:117px;top:202px;width:96px;height:47px}
.consent{position:absolute;left:117px;top:272px;font-size:11px;display:flex;align-items:center;gap:7px}
.box{width:13px;height:13px;border:1px solid #555;display:inline-block;background:var(--white)}
.field{position:absolute;height:41px;width:298px;background:var(--white);box-shadow:0 2px 5px rgba(0,0,0,.14);font-size:14px;color:var(--muted);padding:11px 20px}
.field.area{height:90px;width:610px}

/* menu trio */
.trio{top:927px;height:330px}
.trio-photo{position:absolute;left:0;top:0;width:603px;height:330px;background:radial-gradient(circle at 58% 50%,#d9b04a 0,#8aa75a 22%,#4b3a34 33%,#f4f4f2 35%,#f4f4f2 60%,#7aa57a 100%)}
.panel{position:absolute;left:605px;width:595px;height:108px;padding:10px 14px;background:var(--white);box-shadow:0 1px 3px rgba(0,0,0,.06)}
.panel h3{font-family:'Cinzel',serif;font-weight:700;font-size:19px;color:var(--gold);text-decoration:underline}
.panel p{font-size:12px;color:var(--muted);margin-top:12px}
.panel.gold{background:var(--gold)}
.panel.gold h3,.panel.gold p{color:var(--white)}

/* about */
.about{top:1257px;height:383px}
.about h2{position:absolute;left:63px;top:42px;width:560px;font-family:'Cinzel',serif;font-weight:700;font-size:34px;line-height:46px}
.about p{position:absolute;left:63px;top:160px;width:600px;font-size:12.5px;line-height:20px;color:#444}
.about-photo{position:absolute;left:749px;top:0;width:451px;height:383px;background:linear-gradient(180deg,#e8e6e3 0%,#d9d5cf 55%,#a0653a 80%,#8a5532 100%)}

/* features */
.features{top:1640px;height:170px;background:var(--gold);display:flex;padding:32px 0 0 60px}
.feature{width:230px;padding:0 28px 0 0}
.feature+.feature{border-left:1px solid var(--ink);padding-left:20px;margin-top:16px;padding-top:0}
.feature h4{font-family:'Cinzel',serif;font-weight:700;font-size:14px;margin-bottom:12px}
.feature+.feature h4{margin-top:-16px}
.feature p{font-size:12.5px;line-height:14px}

/* specialities */
.specials{top:1810px;height:254px;background:var(--dark)}
.specials h2{position:absolute;left:64px;top:76px;font-family:'Cinzel',serif;font-weight:700;font-size:40px;line-height:52px;color:var(--gold)}
.dish{position:absolute;top:0;width:213px;height:254px}
.next{position:absolute;left:1120px;top:113px}

/* tip */
.tip{top:2064px;height:368px;background:linear-gradient(90deg,#3f9a6a 0%,#e7a3c3 20%,#f3f3ef 45%,#f3f3ef 60%,#78b58a 80%,#2e8a5a 100%)}
.tip-card{position:absolute;left:188px;top:66px;width:824px;height:250px;background:rgba(255,255,255,.82);text-align:center}
.tip-card h2{font-family:'Cinzel',serif;font-weight:700;font-size:34px;margin-top:18px}
.tip-card h5{font-size:15px;font-weight:500;margin-top:14px}
.tip-card p{font-size:13.5px;line-height:15px;margin-top:18px}
.btn-more{width:112px;height:46px;margin-top:29px}

/* footer */
.site-footer{top:2432px;height:295px;background:var(--black);color:var(--white)}
.f-brand{position:absolute;left:63px;top:40px;width:148px;text-align:center}
.f-brand .brand-name{font-size:18px}
.f-brand .brand-sub{font-size:7px;border-color:var(--white)}
.f-tag{position:absolute;left:53px;top:114px;font-size:12.5px;line-height:14px;color:#ddd}
.f-nav{position:absolute;left:290px;top:36px;font-size:15px;line-height:25px}
.f-map{position:absolute;left:464px;top:35px;width:250px;height:163px;background:linear-gradient(135deg,#eef0f2,#dfe6ec 60%,#e8e3da)}
.newsletter{position:absolute;left:734px;top:36px;width:262px}
.newsletter h6{font-size:15px;font-weight:500}
.nl-input{margin-top:12px;height:37px;background:var(--white);color:var(--muted);font-size:10.5px;padding:11px 12px}
.nl-check{display:flex;align-items:center;gap:8px;font-size:10.5px;margin-top:9px}
.nl-check .box{width:20px;height:20px;border:0}
.btn-sub{margin-top:14px;width:100px;height:40px;border:1px solid var(--gold);color:var(--gold);display:flex;align-items:center;justify-content:center;font-size:14px}
.contact{position:absolute;left:1016px;top:38px;font-size:10.5px}
.c-row{display:flex;gap:14px;align-items:flex-start;margin-bottom:12px}
.c-row svg{flex:none}
.social{display:flex;gap:8px;margin-bottom:14px}
.social span{width:18px;height:18px;border-radius:50%;background:var(--white);display:inline-block}
.copy{position:absolute;left:53px;top:256px;font-size:9.5px;color:#ccc}
.to-top{position:absolute;left:1127px;top:252px}
</style>
</head>
<body>

<header class="site-header">
  <div class="brand"><span class="brand-name">Dulmiro Table</span><span class="brand-sub">CAFE &amp; RESTAURANT</span></div>
  <nav class="nav">
    <span class="active">Úvod</span><span>Denné menu</span><span class="drop">Naša ponuka</span><span class="drop">Eventy</span><span>Rezervácia</span>
  </nav>
  <span class="btn btn-contact">Kontakty</span>
</header>

<section class="hero">
  <div class="hero-photo" role="img" aria-label="Interiér reštaurácie s barom a tyrkysovými sedačkami"></div>
  <div class="hero-shade"></div>
  <h1 class="hero-title">Prinášame zážitok<br>z jedla a skvelej atmosféry</h1>
  <span class="btn hero-btn">Hľadáme do tímu skvelých ľudí</span>
</section>

<section class="reserve">
  <h2>Rezervujte si u nás<br>príjemný zážitok</h2>
  <p>Vyplňte si požiadavky podľa Vašich predstáv pre zážitok v Dulmiro Table</p>
  <span class="btn btn-send">Odoslať</span>
  <div class="consent"><span class="box"></span>Súhlas so spracovaním osobných úd</div>
  <div class="field" style="left:474px;top:54px;font-size:13px">Meno a priezvisko</div>
  <div class="field" style="left:786px;top:54px">Dátum rezervácie</div>
  <div class="field" style="left:474px;top:99px">Email</div>
  <div class="field" style="left:786px;top:99px">Čas príchodu</div>
  <div class="field" style="left:474px;top:144px">Telefón</div>
  <div class="field" style="left:786px;top:144px">Počet ľudí</div>
  <div class="field area" style="left:474px;top:193px;font-size:13px">Vaša správa pre nás</div>
</section>

<section class="trio">
  <div class="trio-photo" role="img" aria-label="Tanier so šalátom a morskými plodmi medzi tropickými listami"></div>
  <div class="panel gold" style="top:0"><h3>Denné menu</h3><p>Každý deň pestrá ponuka jedál z čerstvých surovín. Každý si vyberie a</p></div>
  <div class="panel" style="top:110px"><h3>Naša ponuka</h3><p>Kulinárske skvosty, slovenské špeciality a gastro zážitky z rôznych kútov sveta</p></div>
  <div class="panel" style="top:220px"><h3>Podujatia</h3><p>Tvoríme živý priestor pre stretnutia, zábavu, umenie a zážitkové prednášky</p></div>
</section>

<section class="about">
  <h2>Rezervujte si u nás príjemný zážitok</h2>
  <p>V našej reštaurácii sa snúbi moderná kuchyňa s prvkami tradície, domáce slovenské špeciality s chutnými gastro zážitkami z iných krajín. Koncept a alchýmiu kuchyne Dulmiro Table tvoríme citlivo a interaktívne na základe dlhoročných, zahraničných skúseností i bohatej praxe. Držíme sa pevne našich hodnôt, ako je kvalita, čerstvosť, lokálnosť, sezónnosť. Držíme vysokú úroveň našej práce a každý deň sa snažíme posúvať o krok vpred. Výber jedla môže byť pre Vás v Dulmiro Table výzvou, zážitkom, i dobrodružstvom, pretože každé jedlo je u nás výhrou. Nájdete nás v tichej a príjemnej lokalite Devínskej Novej Vsi. Príďte si urobiť príjemný čas pre telo i dušu. Pozývame Vás. Lenka Hrabovská, majiteľka reštaurácie</p>
  <div class="about-photo" role="img" aria-label="Majiteľka reštaurácie pri prestretom stole"></div>
</section>

<section class="features">
  <div class="feature"><h4>Pokojná atmosféra</h4><p>Príjemná, tichá lokalita v Devínskej Novej Vsi s turistickými, prírodnými skvosťmi</p></div>
  <div class="feature"><h4>Radosť z jedla</h4><p>Príjemná, tichá lokalita v Devínskej Novej Vsi s turistickými, prírodnými skvosťmi</p></div>
  <div class="feature"><h4>Čerstvosť ingrediencií</h4><p>Príjemná, tichá lokalita v Devínskej Novej Vsi s turistickými, prírodnými skvosťmi</p></div>
  <div class="feature"><h4>Vysoká úroveň</h4><p>Príjemná, tichá lokalita v Devínskej Novej Vsi s turistickými, prírodnými skvosťmi</p></div>
  <div class="feature"><h4>Dulmiro know-how</h4><p>Príjemná, tichá lokalita v Devínskej Novej Vsi s turistickými, prírodnými skvosťmi</p></div>
</section>

<section class="specials">
  <h2>Naše<br>špeciality</h2>
  <div class="dish" style="left:348px;background:linear-gradient(135deg,#ece9e4,#d8c79a 50%,#e9e6e1)" role="img" aria-label="Pizza s cviklou a rukolou"></div>
  <div class="dish" style="left:561px;background:linear-gradient(135deg,#e7e5e1,#a8693a 50%,#e6e4e0)" role="img" aria-label="Burger na tanieri"></div>
  <div class="dish" style="left:774px;background:linear-gradient(135deg,#3a3a3a,#5a3a2a 50%,#e5e2dc)" role="img" aria-label="Čokoládový dezert s vanilkovým krémom"></div>
  <div class="dish" style="left:987px;background:linear-gradient(135deg,#ecebe8,#c98d4a 45%,#7a9a4a 70%,#ebeae7)" role="img" aria-label="Šalát s hruškou a syrom"></div>
  <svg class="next" width="22" height="30" viewBox="0 0 22 30"><path d="M5 3 L17 15 L5 27" fill="none" stroke="#111" stroke-width="3"/></svg>
</section>

<section class="tip" role="img" aria-label="Tropické listy a ružové kvety">
  <div class="tip-card">
    <h2>Tip na výlet</h2>
    <h5>SPOZNAJTE KRÁSY DEVÍNSKEJ NOVEJ VSI</h5>
    <p>Na potulkách Devínskou Novou Vsou a jej okolí vás určite osloví jej rozmanitosť, prírodné či kultúrne bohatstvo.<br>Odporúčame navštíviť tieto miesta a možnosti, ako urobiť sebe či rodine príjemný zážitok.</p>
    <span class="btn btn-more">Uč sa viac</span>
  </div>
</section>

<footer class="site-footer">
  <div class="f-brand"><span class="brand-name">Dulmiro Table</span><span class="brand-sub">CAFE &amp; RESTAURANT</span></div>
  <div class="f-tag">Prinášame zážitok<br>z jedla a skvelej atmosféry</div>
  <nav class="f-nav">Úvod<br>Denné menu<br>Naša ponuka<br>Eventy<br>Rezervácia</nav>
  <div class="f-map" role="img" aria-label="Mapa okolia reštaurácie"></div>
  <div class="newsletter">
    <h6>Prihláste sa na odber našich noviniek</h6>
    <div class="nl-input">Sem napíšte svoju emailovú adresu</div>
    <div class="nl-check"><span class="box"></span>Súhlasím so spracovaním osobných údajov</div>
    <div class="nl-check"><span class="box"></span>Súhlasím zo zasielaním newslettra.</div>
    <div class="btn-sub">Odoberať</div>
  </div>
  <div class="contact">
    <div class="social"><span></span><span></span></div>
    <div class="c-row"><svg width="18" height="18" viewBox="0 0 24 24"><path fill="#fff" d="M6.6 10.8a15 15 0 0 0 6.6 6.6l2.2-2.2c.3-.3.7-.4 1-.2 1.1.4 2.3.6 3.6.6.6 0 1 .4 1 1V20c0 .6-.4 1-1 1A17 17 0 0 1 3 4c0-.6.4-1 1-1h3.5c.6 0 1 .4 1 1 0 1.3.2 2.5.6 3.6.1.3 0 .7-.2 1z"/></svg>+421 900 123 456</div>
    <div class="c-row"><svg width="18" height="14" viewBox="0 0 24 18"><path fill="#fff" d="M2 0h20a2 2 0 0 1 2 2v14a2 2 0 0 1-2 2H2a2 2 0 0 1-2-2V2a2 2 0 0 1 2-2zm10 8 10-6H2z"/></svg>info@dulmirotable.sk</div>
    <div class="c-row"><svg width="18" height="20" viewBox="0 0 24 28"><path fill="#fff" d="M12 0a9 9 0 0 1 9 9c0 7-9 17-9 17S3 16 3 9a9 9 0 0 1 9-9zm0 5.5a3.5 3.5 0 1 0 0 7 3.5 3.5 0 0 0 0-7z"/></svg><span>Lipová 12/4<br>841 07 Bratislava<br>Devínska Nová Ves</span></div>
  </div>
  <div class="copy">Copyright © 2024 Dulmiro Table. All Rights Reserved.</div>
  <svg class="to-top" width="20" height="20" viewBox="0 0 20 20"><circle cx="10" cy="10" r="9" fill="none" stroke="#fff" stroke-width="1.3"/><path d="M6 12 L10 7 L14 12z" fill="#fff"/></svg>
</footer>

</body>
</html>
```